Sunridge Lighting Distributors Business Card Design

Use logo and expand the framing box to the extents of the business card. Keep company name in right bottom corner and triangle at top right corner. I would like to have a template so that I can fill in employee name, contact info, email and website.

```html
<!DOCTYPE html>
<html lang="en">
<head>
<meta charset="utf-8">
<title>Sunridge Lighting Distributors – Business Card</title>
<link rel="stylesheet" href="https://fonts.googleapis.com/css2?family=Open+Sans:wght@400;600;700&display=swap">
<style>
  :root {
    --stage: #2b2b2d;
    --card: #1e1e22;
    --panel: #252a32;
    --accent: #1a80c6;
    --ink: #ffffff;
    --ink-soft: #e6e6e6;
    --emboss: #2a2a2f;
    --emboss-edge: #141417;
  }
  * { box-sizing: border-box; margin: 0; padding: 0; }
  html, body { width: 1200px; height: 780px; overflow: hidden; }
  body {
    background: var(--stage);
    font-family: "Open Sans", Arial, sans-serif;
    display: flex;
    align-items: center;
    justify-content: center;
    gap: 40px;
  }
  .card {
    position: relative;
    width: 540px;
    height: 309px;
    background: var(--card);
    overflow: hidden;
    box-shadow: 0 10px 24px rgba(0,0,0,.45);
  }
  .card__shapes { position: absolute; inset: 0; }

  /* front */
  .holder { position: absolute; left: 34px; top: 48px; }
  .holder__name { font-size: 27px; font-weight: 700; color: var(--ink); line-height: 1.1; }
  .holder__first { color: var(--accent); }
  .holder__role { margin-top: 6px; font-size: 14px; color: var(--ink-soft); }

  .company {
    position: absolute; left: 262px; top: 40px; width: 160px;
    display: flex; align-items: flex-start; gap: 10px;
  }
  .company__square { flex: none; width: 14px; height: 14px; background: var(--ink); margin-top: 5px; }
  .company__name {
    font-size: 19px; font-weight: 700; color: var(--ink);
    line-height: 1.15; text-transform: uppercase;
  }

  .contacts {
    position: absolute; left: 250px; top: 170px;
    list-style: none; font-size: 14px; color: var(--ink); line-height: 1.55;
  }
  .contacts li { display: flex; align-items: center; gap: 8px; }
  .contacts svg { width: 13px; height: 13px; fill: var(--accent); flex: none; }

  .address-band {
    position: absolute; left: 0; right: 0; bottom: 0; height: 38px;
    background: var(--accent); color: var(--ink);
    font-size: 14px; display: flex; align-items: center; padding-left: 34px;
  }

  /* back */
  .card--back .back-name {
    position: absolute; inset: 0;
    display: flex; align-items: center; justify-content: center; gap: 14px;
  }
  .back-name__square { width: 22px; height: 22px; background: var(--emboss); }
  .back-name__text {
    font-size: 30px; font-weight: 700; color: var(--emboss);
    text-transform: uppercase; line-height: 1.1;
  }
</style>
</head>
<body>

  <section class="card card--front" aria-label="Business card front">
    <svg class="card__shapes" viewBox="0 0 540 309" aria-hidden="true">
      <polygon points="420,0 540,0 540,271 400,271 400,80" fill="var(--panel)"/>
      <line x1="175" y1="238" x2="240" y2="170" stroke="var(--ink-soft)" stroke-width="1"/>
    </svg>

    <div class="holder">
      <p class="holder__name"><span class="holder__first">Marta</span> Velinova</p>
      <p class="holder__role">Managing Director</p>
    </div>

    <div class="company">
      <span class="company__square"></span>
      <p class="company__name">Sunridge Lighting Distributors</p>
    </div>

    <ul class="contacts">
      <li>
        <svg viewBox="0 0 24 24"><path d="M6.6 10.8a15.1 15.1 0 0 0 6.6 6.6l2.2-2.2a1 1 0 0 1 1-.25 11.4 11.4 0 0 0 3.6.57 1 1 0 0 1 1 1V20a1 1 0 0 1-1 1A17 17 0 0 1 3 4a1 1 0 0 1 1-1h3.5a1 1 0 0 1 1 1c0 1.25.2 2.45.57 3.57a1 1 0 0 1-.25 1z"/></svg>
        (555) 214-3086
      </li>
      <li>
        <svg viewBox="0 0 24 24"><path d="M2 5h20v14H2zm2 2v.5l8 5 8-5V7zm0 2.8V17h16V9.8l-8 5z"/></svg>
        info@website.com
      </li>
      <li>
        <svg viewBox="0 0 24 24"><path d="M12 2a10 10 0 1 0 0 20 10 10 0 0 0 0-20zm6.9 6h-3a15.6 15.6 0 0 0-1.3-3.8A8 8 0 0 1 18.9 8zM12 4c.8 1.2 1.5 2.5 1.9 4h-3.8c.4-1.5 1.1-2.8 1.9-4zM4.3 14a8 8 0 0 1 0-4h3.4a16.5 16.5 0 0 0 0 4zm.8 2h3a15.6 15.6 0 0 0 1.3 3.8A8 8 0 0 1 5.1 16zm3-8h-3a8 8 0 0 1 4.3-3.8A15.6 15.6 0 0 0 8.1 8zM12 20c-.8-1.2-1.5-2.5-1.9-4h3.8c-.4 1.5-1.1 2.8-1.9 4zm2.3-6H9.7a14.7 14.7 0 0 1 0-4h4.6a14.7 14.7 0 0 1 0 4zm.3 5.8a15.6 15.6 0 0 0 1.3-3.8h3a8 8 0 0 1-4.3 3.8zm1.7-5.8a16.5 16.5 0 0 0 0-4h3.4a8 8 0 0 1 0 4z"/></svg>
        www.website.com
      </li>
    </ul>

    <p class="address-band">4210 Harlow Ct #12, Riverton, FL 32100, USA</p>
  </section>

  <section class="card card--back" aria-label="Business card back">
    <div class="back-name">
      <span class="back-name__square"></span>
      <p class="back-name__text">Sunridge<br>Lighting<br>Distributors</p>
    </div>
  </section>

</body>
</html>
```